Stationery Design Project - Professional Training Company

Full set of statinery in PDF and format that can be given to the printers

Letterhead
Business cards x 3
Compliments slip
Envelope
Updates

Many thanks for all your contributions, the quality of the designs is amazing.

Thank you all so much for your contribution to this project, I am very impressed with the designs and choice of designs, you are all clearly very talented individuals.

I hope to be making a decision on the final choice this evening UAE time.

Best regards and again thank you so much

Gordon

I would like to take this opportunity to thank you all for your contributions, I have been very impressed with each of the designs submitted.

I will shortly go back and give each of you a personal rating on each of your designs.

Again thank you all so much for your efforts

Best Regards

Gordon

Target Market(s)

We are a training company that provides IT training for Medical and Professional Staff, we train professional adults

Industry/Entity Type

Business

Requirements
Must have
• The letterhead and compliments slip must have at the bottom of the page:-

Bright Ledger Pathways LLP operates as a limited liability partnership registered in England and Wales (with registered number OC702614)

Business Cards are to be made up for three people (details of those to be provided after appoval of design but are included in this project) and should contain:

Name
Title
Telephone
email
Address: P.O. Box 418263 Dubai UAE
web address: www.brightledgerpathways.example
Nice to have
• Very clean and professional looking
Should not have
• No look to busy or ovr crowded

```html
<!DOCTYPE html>
<html lang="en">
<head>
<meta charset="utf-8">
<title>Business card designs – Bright Ledger Pathways LLP</title>
<link rel="stylesheet" href="https://fonts.googleapis.com/css2?family=Source+Sans+3:wght@400;600;700&display=swap">
<style>
  :root {
    --purple: #7a14c4;
    --green: #259b06;
    --bright-green: #55d61e;
    --mint: #d8f5d0;
    --ink: #231f20;
    --grey-text: #333333;
    --heading-grey: #6d6e71;
    --crop: #7f7f7f;
    --card-edge: #a7a9ac;
    --paper: #ffffff;
  }
  * { margin: 0; padding: 0; box-sizing: border-box; }
  html, body { width: 977px; height: 1200px; overflow: hidden; background: var(--paper); }
  body { position: relative; font-family: "Source Sans 3", "Myriad Pro", Arial, sans-serif; color: var(--grey-text); }

  .card { position: absolute; width: 372px; height: 226px; overflow: hidden; }
  .card--front { left: 53px; background: var(--paper); border: 1px solid var(--card-edge); }
  .card--rear { left: 570px; }

  .row-1 { top: 42px; }
  .row-2 { top: 451px; }
  .row-3 { top: 846px; }

  .brand { position: absolute; display: flex; align-items: center; gap: 8px; color: var(--ink); font-weight: 700; white-space: nowrap; }
  .brand__mark { width: 14px; height: 14px; border-radius: 50%; background: var(--purple); flex: none; }

  .name-band { position: absolute; left: 0; right: 0; top: 113px; height: 34px; background: var(--purple); color: #fff; text-align: center; line-height: 1.05; padding-top: 2px; }
  .person-name { font-size: 15px; font-weight: 600; }
  .person-title { font-size: 12.5px; }

  .contact { position: absolute; left: 0; right: 0; text-align: center; font-size: 12.5px; line-height: 1.2; color: var(--grey-text); }

  .top-strip { position: absolute; left: 0; right: 0; top: 0; height: 11px; background: var(--purple); }
  .contact-band { position: absolute; left: 0; right: 0; bottom: 0; height: 38px; background: var(--green); color: #fff; text-align: center; font-size: 12.5px; line-height: 1.2; padding-top: 4px; }
  .person-corner { position: absolute; right: 14px; top: 16px; text-align: right; color: var(--ink); line-height: 1.05; }

  .rear-fill--mint { width: 100%; height: 100%; background: var(--mint); display: flex; align-items: center; justify-content: center; }
  .rear-fill--purple { width: 100%; height: 100%; background: linear-gradient(115deg, var(--purple), #8d2ad6); }
  .rear-fill--green { width: 100%; height: 100%; background: linear-gradient(180deg, var(--bright-green), #4cc91a); }

  .caption { position: absolute; font-size: 10px; line-height: 1.6; color: var(--ink); }
  .section-title { position: absolute; left: 73px; font-size: 32px; font-weight: 400; color: var(--heading-grey); }

  .crop { position: absolute; background: var(--crop); }
  .crop--h { height: 1px; width: 26px; }
  .crop--v { width: 1px; height: 72px; }
</style>
</head>
<body>

  <!-- Design 1 -->
  <section class="card card--front row-1" aria-label="Business card 1 front">
    <div class="brand" style="left:44px; top:50px; font-size:18px;"><span class="brand__mark"></span>Bright Ledger Pathways LLP</div>
    <div class="name-band">
      <div class="person-name">Your Name</div>
      <div class="person-title">Designation</div>
    </div>
    <div class="contact" style="top:170px;">Address: P.O. Box 418263 Dubai UAE<br>web address: www.brightledgerpathways.example</div>
  </section>
  <section class="card card--rear row-1" aria-label="Business card 1 rear">
    <div class="rear-fill--mint">
      <div class="brand" style="position:static; font-size:20px;"><span class="brand__mark"></span>Bright Ledger Pathways LLP</div>
    </div>
  </section>
  <p class="caption" style="left:67px; top:288px;">Business card - Front Side<br>Size: 9x5.5cm</p>
  <p class="caption" style="left:584px; top:291px;">Business card - Rear Side</p>

  <h2 class="section-title" style="top:376px;">Business card</h2>

  <!-- Design 2 -->
  <section class="card card--front row-2" aria-label="Business card 2 front">
    <div class="top-strip"></div>
    <div class="person-corner">
      <div class="person-name">Your Name</div>
      <div class="person-title">Designation</div>
    </div>
    <div class="brand" style="left:82px; top:94px; font-size:15px;"><span class="brand__mark"></span>Bright Ledger Pathways LLP</div>
    <div class="contact-band">Address: P.O. Box 418263 Dubai UAE<br>web address: www.brightledgerpathways.example</div>
  </section>
  <section class="card card--rear row-2" aria-label="Business card 2 rear">
    <div class="rear-fill--purple" role="img" aria-label="Purple back with a pattern of thin white diagonal lines"></div>
  </section>
  <p class="caption" style="left:67px; top:697px;">Business card - Front Side<br>Size: 9x5.5cm</p>
  <p class="caption" style="left:584px; top:703px;">Business card - Rear Side</p>

  <h2 class="section-title" style="top:771px;">Business card</h2>

  <!-- Design 3 -->
  <section class="card card--front row-3" aria-label="Business card 3 front">
    <div class="brand" style="left:44px; top:58px; font-size:18px;"><span class="brand__mark"></span>Bright Ledger Pathways LLP</div>
    <div class="contact" style="top:113px; color:var(--ink);">
      <div class="person-name">Your Name</div>
      <div class="person-title">Designation</div>
    </div>
    <div class="contact" style="top:170px;">Address: P.O. Box 418263 Dubai UAE<br>web address: www.brightledgerpathways.example</div>
  </section>
  <section class="card card--rear row-3" aria-label="Business card 3 rear">
    <div class="rear-fill--green" role="img" aria-label="Bright green back with a pattern of thin white horizontal stripes"></div>
  </section>
  <p class="caption" style="left:67px; top:1091px;">Business card - Front Side<br>Size: 9x5.5cm</p>
  <p class="caption" style="left:584px; top:1096px;">Business card - Rear Side</p>

  <!-- Crop marks -->
  <div class="crop crop--h" style="left:0; top:42px;"></div>
  <div class="crop crop--h" style="left:0; top:267px;"></div>
  <div class="crop crop--h" style="left:452px; top:42px;"></div>
  <div class="crop crop--h" style="left:452px; top:267px;"></div>
  <div class="crop crop--v" style="left:424px; top:274px;"></div>
  <div class="crop crop--v" style="left:570px; top:274px;"></div>
  <div class="crop crop--h" style="left:0; top:451px;"></div>
  <div class="crop crop--h" style="left:0; top:678px;"></div>
  <div class="crop crop--h" style="left:452px; top:451px;"></div>
  <div class="crop crop--h" style="left:452px; top:678px;"></div>
  <div class="crop crop--h" style="left:951px; top:451px;"></div>
  <div class="crop crop--v" style="left:424px; top:685px;"></div>
  <div class="crop crop--v" style="left:570px; top:685px;"></div>
  <div class="crop crop--v" style="left:424px; top:372px; height:52px;"></div>
  <div class="crop crop--v" style="left:570px; top:372px; height:52px;"></div>
  <div class="crop crop--h" style="left:0; top:846px;"></div>
  <div class="crop crop--h" style="left:0; top:1072px;"></div>
  <div class="crop crop--h" style="left:452px; top:846px;"></div>
  <div class="crop crop--h" style="left:452px; top:1072px;"></div>
  <div class="crop crop--v" style="left:424px; top:766px; height:52px;"></div>
  <div class="crop crop--v" style="left:570px; top:766px; height:52px;"></div>
  <div class="crop crop--v" style="left:424px; top:1080px;"></div>
  <div class="crop crop--v" style="left:570px; top:1080px;"></div>

</body>
</html>
```